Create a Graphic About YOURSELF and PixelHarbor

PixelHarbor would like you (designers) to create an awesome graphic to promote YOURSELF and your profile on PixelHarbor!

Your graphic should communicate your name, your services and should mention PixelHarbor.

The design should be perfect for sharing on Chatterly. Here's an example of what we'd like http://blog.pixelharbor-example.ca/article/333/pixelharbor-launches-3000-hire-me-social-design-contest

Once you submitted your design, we'd love you to share the design ('advertisement') and promote yourself and PixelHarbor to your friends and potential customers. So make your submissions great and get your friends to vote for your design by 'Liking' it on Chatterly!

Prizes:
$1500 - "PixelHarbor Community" prize awarded to the designer with the most Chatterly 'Likes'
5 x $50 for the next 5 'most liked' designs on Chatterly

$1000 - "Hire Me" prize awarded to the designer who receives the most client invites
5 x $50 for the next 5 'most invited' designers

In summary, this is a great opportunity for you to increase your exposure to PixelHarbor customers and win cash prizes. Show off your design skills and get hired by PixelHarbor customers from around the world!

Target Market(s)

Fans, friends and customers of YOU

Industry/Entity Type

Cash

Requirements
Must have
• 1) Include your PixelHarbor user name on the graphic so customers can find you in the PixelHarbor Designer Directory
2) Include the tagline "Hire Me on PixelHarbor.com!" in your graphic design.
3) Share your design's URL on our Chatterly wall at http://chatterly-example.com/pixelharbor and get your friends to 'like' your design.
Nice to have
• 1) Include a tagline that expresses your design approach/philosophy
2) Artwork dimensions: 403 x 403 px
3) You can submit more than 1 design!
Should not have
• You must own the copyright of any images you use including stock imagery.

```html
<!DOCTYPE html>
<html lang="en">
<head>
<meta charset="utf-8">
<title>Brightmarque Designs – Hire Me</title>
<link rel="stylesheet" href="https://fonts.googleapis.com/css2?family=Montserrat:wght@400;500;700;800&family=Questrial&display=swap">
<style>
  :root {
    --bg-edge: #16191c;
    --bg-glow: #3c5c62;
    --bg-warm: #3e2227;
    --ink: #ffffff;
    --ink-soft: #e6e8ea;
    --ink-muted: #b9bcbf;
    --accent-red: #e01a1a;
    --plate: #ffffff;
  }
  * { margin: 0; padding: 0; box-sizing: border-box; }
  html, body { width: 1200px; height: 1200px; overflow: hidden; background: var(--bg-edge); }
  .poster {
    position: relative;
    width: 1200px; height: 1200px;
    overflow: hidden;
    font-family: "Montserrat", sans-serif;
    color: var(--ink);
    background:
      radial-gradient(ellipse 620px 480px at 580px 160px, var(--bg-glow) 0%, rgba(60,92,98,0.35) 50%, rgba(0,0,0,0) 100%),
      radial-gradient(ellipse 760px 520px at 560px 1120px, var(--bg-warm) 0%, rgba(62,34,39,0.4) 55%, rgba(0,0,0,0) 100%),
      linear-gradient(180deg, #1f2a2d 0%, #1c1f22 50%, #241a1d 100%);
  }
  .brand-name {
    position: absolute; left: 110px; top: 92px; width: 960px;
    font-size: 92px; font-weight: 700; line-height: 100px;
    color: var(--ink); letter-spacing: 1px;
  }
  .rule { position: absolute; left: 110px; width: 954px; height: 3px; background: var(--ink); }
  .rule--bottom { top: 840px; }
  .contact { position: absolute; left: 110px; }
  .contact__label { font-size: 25px; font-weight: 500; color: var(--ink-soft); line-height: 28px; }
  .contact__value { font-size: 26px; font-weight: 700; color: var(--ink); line-height: 30px; letter-spacing: 0.3px; }
  .contact--email { top: 362px; }
  .contact--callsy { top: 434px; }
  .status { position: absolute; left: 110px; top: 600px; }
  .status__label { font-size: 34px; font-weight: 400; color: var(--ink); line-height: 42px; }
  .status__value { font-size: 34px; font-weight: 800; color: var(--accent-red); line-height: 40px; letter-spacing: 1px; }
  .services {
    position: absolute; right: 136px; top: 342px; list-style: none; text-align: right;
    font-family: "Questrial", sans-serif; font-size: 80px; line-height: 92px; color: var(--ink-soft);
  }
  .more-tag {
    position: absolute; left: 706px; top: 843px; width: 366px; height: 56px;
    background: var(--plate); color: #111;
    font-weight: 700; font-size: 44px; line-height: 56px; text-align: center;
  }
  .philosophy {
    position: absolute; left: 110px; top: 922px; list-style: none;
    font-size: 44px; line-height: 46px; font-weight: 400; color: var(--ink);
  }
  .philosophy b { font-weight: 800; }
  .hire { position: absolute; left: 790px; top: 986px; width: 290px; text-align: center; }
  .hire__label { font-size: 30px; font-weight: 800; letter-spacing: 5px; color: var(--ink-muted); line-height: 40px; }
  .hire__site {
    margin-top: 8px; display: flex; align-items: center; justify-content: center; gap: 12px;
    font-size: 40px; font-weight: 500; color: var(--ink-muted); line-height: 48px;
  }
  .hire__dot { width: 26px; height: 26px; border-radius: 50%; background: var(--ink-muted); }
</style>
</head>
<body>
<main class="poster">
  <h1 class="brand-name">BRIGHTMARQUE<br>DESIGNS</h1>

  <div class="contact contact--email">
    <p class="contact__label">Email</p>
    <p class="contact__value">BRIGHTMARQUEDESIGN@MAILBOX-EXAMPLE.COM</p>
  </div>
  <div class="contact contact--callsy">
    <p class="contact__label">Callsy</p>
    <p class="contact__value">BRIGHTMARQUEDESIGN</p>
  </div>

  <div class="status">
    <p class="status__label">Curent Work Status</p>
    <p class="status__value">OPEN</p>
  </div>

  <ul class="services">
    <li>Print</li>
    <li>Web</li>
    <li>Logo</li>
    <li>Graphics</li>
    <li>Illustration</li>
  </ul>

  <div class="rule rule--bottom"></div>
  <div class="more-tag">and more...</div>

  <ul class="philosophy">
    <li><b>S</b>imple</li>
    <li><b>I</b>nnovative</li>
    <li><b>U</b>nique</li>
    <li><b>S</b>tylish</li>
  </ul>

  <div class="hire">
    <p class="hire__label">HIRE ME</p>
    <p class="hire__site"><span class="hire__dot"></span>PixelHarbor</p>
  </div>
</main>
</body>
</html>
```